Tattoo Removal & Cosmetic Tattoo

Include Logo (as attached)
include picture of girl (as attached) but please crop body off and zoom in on head and arms please
Include the following:-
Helena Dorvik
Shop 8 FF, 2316 Parvell Road, Coolum Beach 4581
Phone: 0417826395
Email: helena@velburo.com.au

```html
<!DOCTYPE html>
<html lang="en">
<head>
<meta charset="utf-8">
<title>Velburo – Tattoo Removal &amp; Cosmetic Tattoo</title>
<link rel="stylesheet" href="https://fonts.googleapis.com/css2?family=Oswald:wght@400;500;600&family=Lilita+One&display=swap">
<style>
  :root {
    --ink-black: #000000;
    --lime: #8cc63f;
    --white: #ffffff;
    --photo-light: #b9c6d8;
    --photo-mid: #7b8aa3;
    --photo-dark: #3b4050;
    --photo-skin: #d9b8a6;
  }
  html, body {
    margin: 0;
    padding: 0;
    overflow: hidden;
    background: var(--ink-black);
  }
  .card {
    position: relative;
    width: 669px;
    height: 1200px;
    background: var(--ink-black);
    overflow: hidden;
    font-family: "Oswald", "Arial Narrow", sans-serif;
    color: var(--white);
  }
  .brand {
    position: absolute;
    top: 50px;
    left: 0;
    width: 100%;
    text-align: center;
  }
  .brand-name {
    margin: 0;
    font-family: "Oswald", "Arial Narrow", sans-serif;
    font-weight: 500;
    font-size: 104px;
    line-height: 1;
    letter-spacing: 6px;
    color: var(--white);
  }
  .tagline {
    margin: 22px 0 0;
    font-weight: 500;
    font-size: 29px;
    letter-spacing: 1.5px;
    color: var(--lime);
    text-transform: uppercase;
  }
  .tagline-rule {
    width: 560px;
    height: 2px;
    margin: 8px auto 0;
    background: var(--lime);
  }
  .features {
    display: flex;
    justify-content: center;
    gap: 22px;
    margin-top: 8px;
    font-weight: 500;
    font-size: 20px;
    letter-spacing: 1px;
    text-transform: uppercase;
  }
  .feature {
    display: flex;
    align-items: center;
    gap: 6px;
  }
  .feature svg { width: 20px; height: 20px; }
  .portrait-frame {
    position: absolute;
    left: 56px;
    top: 308px;
    width: 557px;
    height: 557px;
    border-radius: 50%;
    background: var(--lime);
    padding: 13px;
    box-sizing: border-box;
  }
  .portrait {
    width: 100%;
    height: 100%;
    border-radius: 50%;
    background:
      radial-gradient(circle at 48% 42%, var(--photo-skin) 0 16%, transparent 30%),
      radial-gradient(circle at 30% 25%, var(--photo-light) 0 20%, transparent 45%),
      linear-gradient(160deg, var(--photo-mid), var(--photo-dark));
  }
  .contact {
    position: absolute;
    left: 0;
    top: 962px;
    width: 100%;
    text-align: center;
    font-size: 28px;
    line-height: 38px;
    letter-spacing: 0.5px;
  }
  .contact p { margin: 0; }
  .person-name {
    font-family: "Lilita One", "Arial Black", sans-serif;
    font-size: 33px;
    letter-spacing: 1px;
    color: var(--lime);
    margin-bottom: 2px !important;
  }
  .address { margin-bottom: 38px !important; }
  .base-band {
    position: absolute;
    left: 0;
    bottom: 0;
    width: 100%;
    height: 12px;
    background: var(--lime);
  }
</style>
</head>
<body>
<main class="card">
  <header class="brand">
    <h1 class="brand-name">VELBURO</h1>
    <p class="tagline">Tattoo Removal &amp; Cosmetic Tattoo</p>
    <div class="tagline-rule"></div>
    <div class="features">
      <span class="feature">
        <svg viewBox="0 0 20 20" aria-hidden="true"><polyline points="3,11 8,16 17,4" fill="none" stroke="#8cc63f" stroke-width="3" stroke-linecap="round" stroke-linejoin="round"/></svg>
        Pain Free
      </span>
      <span class="feature">
        <svg viewBox="0 0 20 20" aria-hidden="true"><polygon points="12,1 4,11 9,11 7,19 16,8 11,8" fill="#8cc63f"/></svg>
        Non Laser
      </span>
    </div>
  </header>

  <div class="portrait-frame">
    <div class="portrait" role="img" aria-label="Portrait photo of a tattooed woman with silver-blue hair, cropped to head and arms"></div>
  </div>

  <section class="contact">
    <p class="person-name">Helena Dorvik</p>
    <p>Shop 8 FF, 2316 Parvell Road</p>
    <p class="address">Coolum Beach 4581</p>
    <p>Phone: 0417826395</p>
    <p>Email: helena@velburo.com.au</p>
  </section>

  <div class="base-band"></div>
</main>
</body>
</html>
```